Building company buisness cards

We are looking for a sharp modern new look for our business cards.
We are a New Zealand based company that specialises in house and land packages.
We have attached a photo of the current logo and would like to see if it can be improved somehow if needed.
We are open to any colours but we have chosen green at this stage.
Feel free to change the font and make the logo smarter looking.
Play with the colours and see what looks best.

We want a card that looks so good know one will want to throw it away!

Target Market(s)

Home buyers

Industry/Entity Type

Building

Contact Information for Business Card

Dorian Keswick
0217392604
dkeswick@tidewellhomecraft.co.nz
tidewellhomecraft.co.nz

Font styles to use
Serif
Sans Serif

Colors

Designer to choose colors to be used in the design.

Requirements
Must have
• Logo and company name on one side, details on the other side
Nice to have
• Color codes for the original green are HEX #4a8028, RGB(74,128,40), CMYK(42,0,69,50)
• Round corners, Raised and/or spot UV

```html
<!DOCTYPE html>
<html lang="en">
<head>
<meta charset="utf-8">
<title>Tidewell Homecraft – Business Cards</title>
<link href="https://fonts.googleapis.com/css2?family=Roboto:wght@400;500;700;900&display=swap" rel="stylesheet">
<style>
  :root {
    --backdrop: #2b2b2b;
    --brand-green: #4a8028;
    --card-white: #ffffff;
    --stripe-grey: #8c8c8c;
    --back-grey: #575757;
    --rule-grey: #8a8a8a;
    --text-light: #ffffff;
  }
  * { margin: 0; padding: 0; box-sizing: border-box; }
  html, body {
    width: 1125px; height: 1200px; overflow: hidden;
    background: var(--backdrop);
    font-family: "Roboto", Arial, sans-serif;
  }
  .canvas { position: relative; width: 1125px; height: 1200px; }
  .card {
    position: absolute; left: 150px; width: 826px; height: 472px;
    border-radius: 23px; overflow: hidden;
  }
  .card--front { top: 98px; background: var(--brand-green); }
  .card--back { top: 631px; background: var(--back-grey); }

  .front-panel { position: absolute; inset: 0; width: 100%; height: 100%; }
  .front-panel .panel-white { fill: var(--card-white); }
  .front-panel .panel-stripe { fill: var(--stripe-grey); }

  .contact { position: absolute; left: 36px; top: 160px; color: var(--text-light); }
  .contact__name {
    font-size: 29px; font-weight: 500; letter-spacing: 0.3px;
    text-transform: uppercase; margin-bottom: 28px;
  }
  .contact__line { font-size: 19px; line-height: 26px; font-weight: 400; }

  .brand-front {
    position: absolute; left: 480px; top: 248px; width: 346px;
    text-align: center; color: var(--brand-green);
    font-size: 38px; font-weight: 700; line-height: 42px;
  }

  .brand-back {
    position: absolute; left: 0; right: 0; top: 188px;
    text-align: center; color: var(--text-light);
  }
  .brand-back__name {
    font-size: 44px; font-weight: 900; line-height: 48px; letter-spacing: -0.5px;
  }
  .brand-back__rule {
    width: 86px; height: 1px; background: var(--rule-grey); margin: 10px auto 10px;
  }
  .brand-back__web { font-size: 19px; font-weight: 400; letter-spacing: 2px; }
</style>
</head>
<body>
<main class="canvas">
  <section class="card card--front">
    <svg class="front-panel" viewBox="0 0 826 472" preserveAspectRatio="none" aria-hidden="true">
      <path class="panel-stripe" d="M550 0 L566 0 L362 204 Q344 236 362 268 L566 472 L550 472 L348 272 Q326 236 348 200 Z"/>
      <path class="panel-white" d="M570 0 L826 0 L826 472 L570 472 L369 271 Q350 236 369 201 Z"/>
    </svg>
    <div class="contact">
      <p class="contact__name">Dorian Keswick</p>
      <p class="contact__line">(P) 0217392604</p>
      <p class="contact__line">dkeswick@tidewellhomecraft.co.nz</p>
      <p class="contact__line">tidewellhomecraft.co.nz</p>
    </div>
    <p class="brand-front">Tidewell<br>Homecraft</p>
  </section>

  <section class="card card--back">
    <div class="brand-back">
      <p class="brand-back__name">tidewell<br>homecraft.</p>
      <div class="brand-back__rule"></div>
      <p class="brand-back__web">www.tidewellhomecraft.co.nz</p>
    </div>
  </section>
</main>
</body>
</html>
```